Fitness company needs new web design

We are looking to get our current site design improved to a newer design to better match our logo and features.

Current Site:
brivanfitco.com

* We would like the site to be modern/simple.
* The site will need to have the ability to take payments via paylune.
* We would like a "shop" page, as we will be selling supplements. Possible linkup with Cartwell.
* The main landing page should flow in a way to sell our personal training & diet services. We would like the user to have to input their info (like we currently have) before placing an order.

We like how this site is put together: lumaxrt.com

We use this service for our mobile app that our clients get to use when they signup: coachvelo.net

If you have any questions please message use before starting your design.

Target Market(s)

Weight Loss, Fitness, Sports Athletes

Industry/Entity Type

Fitness

Coding

Coded - Design and coding required

Number of Pages Required

5+ page

Colors

Designer to choose colors to be used in the design.

Requirements
Must have
• Menu Tabs:
• - Programs
• - We offer 3 programs (see below for complete details)
• * Basic
• * Premium
• * Elite
• - Supplements
• - We currently have 2 supplements (see attached labels)
• * Nova Lift
• * Nova Flare
• - About
• - FAQ
• - Contact
• - Book Appointment (bookwisp.com)
• Program Breakdown:
• Basic: Price $99/month
• - One 30 Minute In-Person or Phone Consultation
• - Unlimited in-app text support
• - Basic Nutrition Education
• - 30 Day Meal Plan
• Premium: Price $149/month
• - Two 30 Minute In-Person or Phone Consultations
• - Unlimited In-App Messaging Support
• - Customized Strength Training Program
• - Each Exercise Demonstrated in HD Videos
• - Personalized Cardio Program
• - Personalized Nutrition Coaching & Meal Plans
• Elite: Price $249/month
• - Weekly 30 Minute In-Person or Phone Consultation
• - Weekly Customized Strength Training Program
• - Weekly Customized Cardio Training Program
• - Bi-Weekly Nutrition Coaching & Meal Plans
Nice to have
• Click through form that collects clients information (like we have on our current site brivanfitco.com

```html
<!DOCTYPE html>
<html lang="en">
<head>
<meta charset="utf-8">
<title>Brivan Fitco — Personal Training &amp; Nutrition</title>
<link href="https://fonts.googleapis.com/css2?family=Montserrat:wght@500;600;700;800&family=Nunito+Sans:wght@400;600;700&display=swap" rel="stylesheet">
<style>
:root{
  --yellow:#eef20a;
  --ink:#1c1c1c;
  --dark:#161616;
  --dark-2:#222222;
  --grey:#6b6b6b;
  --light:#f4f4f4;
  --white:#ffffff;
  --line:#d9d9d9;
}
*{margin:0;padding:0;box-sizing:border-box}
html,body{width:1200px;height:4660px;overflow:hidden}
body{font-family:"Nunito Sans",Arial,sans-serif;color:var(--ink);background:var(--white);position:relative}
h1,h2,h3,h4,.nav,.btn{font-family:"Montserrat",Arial,sans-serif}
section,header,footer{position:absolute;left:0;width:1200px;overflow:hidden}
.abs{position:absolute}
.photo{position:absolute}
.hl{color:var(--yellow)}
.btn{display:inline-block;font-weight:700;font-size:13px;letter-spacing:.5px;text-transform:uppercase}
.btn-yellow{background:var(--yellow);color:var(--ink);padding:12px 26px}
.btn-outline{border:2px solid var(--ink);border-radius:20px;padding:8px 18px;color:var(--ink);font-size:12px}
.btn-outline.light{border-color:var(--white);color:var(--white)}

/* header */
.site-header{top:0;height:100px;background:var(--white)}
.logo-block{position:absolute;left:0;top:0;width:300px;height:100px;background:#cfcfcf;clip-path:polygon(0 0,100% 0,78% 100%,0 100%)}
.logo{position:absolute;left:40px;top:36px;font-family:"Nunito Sans",sans-serif;font-weight:700;font-size:20px;color:var(--ink)}
.nav{position:absolute;right:40px;top:0;height:74px;display:flex;align-items:center;gap:28px;font-size:14px;font-weight:700;color:var(--ink)}
.cart{display:flex;align-items:center;gap:6px}

/* hero */
.hero{top:100px;height:560px;background:var(--dark)}
.hero-photo{left:0;top:0;width:1200px;height:560px;background:radial-gradient(ellipse at 28% 45%,#5b4e48 0%,#2e2a28 40%,#141414 80%)}
.hero-copy{position:absolute;left:656px;top:96px;width:480px;color:var(--white)}
.hero-copy h1{font-size:38px;font-weight:800;line-height:1.15;text-transform:uppercase}
.hero-copy p{margin:22px 0 26px;font-size:15px;line-height:1.6;color:#e4e4e4;width:420px}
.dots{display:flex;gap:8px;margin-top:34px}
.dots i{width:14px;height:14px;border:2px solid var(--white);border-radius:50%}
.dots i.on{background:var(--white)}

/* welcome */
.welcome{top:660px;height:500px;background:var(--white)}
.welcome-photo{left:40px;top:60px;width:560px;height:400px;background:linear-gradient(135deg,#eceae6,#d8cfc5 55%,#8fb8a8)}
.welcome-copy{position:absolute;left:640px;top:105px;width:500px}
.kicker{font-family:"Montserrat",sans-serif;font-weight:700;font-size:24px;color:#d7dc00;text-transform:uppercase}
.welcome-copy h2{font-size:40px;font-weight:800;margin-bottom:18px}
.welcome-copy p{font-size:15px;line-height:1.65;color:var(--grey);margin-bottom:22px}

/* help */
.help{top:1160px;height:560px;background:var(--dark)}
.help h2{position:absolute;left:88px;top:156px;width:520px;font-size:31px;font-weight:800;color:var(--white);text-transform:uppercase;line-height:1.25}
.features{position:absolute;left:80px;top:280px;display:flex;gap:38px}
.feature{width:120px;text-align:center;color:var(--white);font-family:"Montserrat",sans-serif;font-weight:700;font-size:12px;text-transform:uppercase;line-height:1.35}
.ring{width:64px;height:64px;border:2px solid var(--white);border-radius:50%;margin:0 auto 14px;display:flex;align-items:center;justify-content:center}
.help-video{left:628px;top:128px;width:504px;height:330px;background:linear-gradient(160deg,#d9dcd8,#a7aba6 60%,#6d706b);border:4px solid var(--white)}
.play{position:absolute;left:50%;top:50%;width:64px;height:64px;margin:-32px 0 0 -32px;border-radius:50%;background:var(--white);display:flex;align-items:center;justify-content:center}

/* discover */
.discover{top:1720px;height:560px;background:var(--white)}
.discover-video{left:110px;top:152px;width:500px;height:256px;background:linear-gradient(120deg,#6b7a4d,#a7925b 50%,#4d5b38);border:4px solid var(--white)}
.discover-copy{position:absolute;left:706px;top:150px;width:440px;color:var(--white)}
.discover-copy h2{font-size:30px;font-weight:800;text-transform:uppercase;line-height:1.25}
.discover-copy p{font-size:13px;line-height:1.6;color:#cfcfcf;margin:18px 0 20px}

/* success */
.success{top:2280px;height:860px;background:var(--white)}
.success h2{position:absolute;left:0;width:1200px;top:126px;text-align:center;font-size:32px;font-weight:800;text-transform:uppercase}
.success .sub{position:absolute;left:0;width:1200px;top:176px;text-align:center;font-size:17px;color:#444}
.success-photo{left:440px;top:240px;width:320px;height:580px;background:linear-gradient(180deg,#e6e6e6,#cbbfb5 45%,#3a3a3a)}
.perk{position:absolute;width:300px}
.perk-head{display:flex;align-items:center;gap:16px;margin-bottom:14px}
.perk h3{font-family:"Nunito Sans",sans-serif;font-weight:600;font-size:18px;line-height:1.3}
.perk p{font-size:13px;line-height:1.6;color:var(--grey)}
.perk.left .perk-head{justify-content:flex-end;text-align:right}
.perk.left p{text-align:right}

/* testimonial */
.testimonial{top:3140px;height:520px;background:radial-gradient(ellipse at 50% 40%,#2c2c2c,#101010 75%)}
.testimonial h2{position:absolute;left:0;width:1200px;top:120px;text-align:center;font-size:32px;font-weight:800;text-transform:uppercase}
.clients{position:absolute;left:210px;top:204px;display:flex;gap:96px}
.client{display:flex;align-items:center;gap:18px;color:var(--white)}
.avatar{width:96px;height:96px;border-radius:50%;border:4px solid var(--white);background:linear-gradient(135deg,#9c8672,#5a4a3e)}
.client b{display:block;font-family:"Montserrat",sans-serif;font-size:15px;color:var(--yellow)}
.client span{font-size:13px}
.quote{position:absolute;left:260px;width:680px;top:338px;text-align:center;color:#d6d6d6;font-size:14px;line-height:1.7}
.t-dots{position:absolute;left:572px;top:430px;display:flex;gap:8px}
.t-dots i{width:12px;height:4px;background:#777}
.t-dots i.on{background:var(--yellow);width:20px}

/* guarantee */
.guarantee{top:3660px;height:600px;background:linear-gradient(90deg,#8a5c44,#b07a5e 45%,#d4d0cb)}
.guarantee-photo{left:0;top:0;width:1200px;height:600px;background:linear-gradient(100deg,rgba(40,60,55,.55),rgba(180,120,95,.25) 35%,rgba(230,230,230,.55) 70%)}
.card{position:absolute;left:536px;top:84px;width:536px;background:var(--white);padding:42px 46px 40px;box-shadow:0 10px 30px rgba(0,0,0,.25)}
.card h2{font-size:38px;font-weight:800;line-height:1.15}
.card p{font-size:16px;line-height:1.6;color:#333;margin:18px 0 26px}

/* footer */
.site-footer{top:4260px;height:400px;background:var(--dark)}
.f-col{position:absolute;top:64px;color:var(--white)}
.f-col h4{font-size:17px;font-weight:700;text-transform:uppercase;margin-bottom:18px}
.f-col li{list-style:none;font-size:13px;color:#d0d0d0;margin-bottom:8px;display:flex;align-items:flex-start;gap:10px}
.bullet{width:5px;height:5px;background:var(--yellow);border-radius:50%;margin-top:7px}
.f-col p{font-size:12px;color:#bbb;line-height:1.55;width:460px}
.form{display:grid;grid-template-columns:220px 220px;gap:12px;margin-top:18px}
.field{height:38px;border:1px solid #555;background:transparent;color:#999;font-size:12px;padding:10px 12px}
.socials{position:absolute;left:0;width:1200px;top:304px;display:flex;justify-content:center;gap:10px}
.socials i{width:22px;height:22px;border:1px solid #999;border-radius:50%}
.copy{position:absolute;left:0;width:1200px;top:344px;text-align:center;color:#999;font-size:12px}
</style>
</head>
<body>

<header class="site-header">
  <div class="logo-block"></div>
  <div class="logo">Brivan Fitco</div>
  <nav class="nav">
    <span>HOME</span><span>ABOUT US</span><span>PROGRAMS</span><span>SUPPLEMENTS</span><span>FAQ</span><span>CONTACT US</span>
    <span class="cart">
      <svg width="22" height="20" viewBox="0 0 22 20"><path d="M1 2h3l3 11h11l3-8H6" fill="none" stroke="#1c1c1c" stroke-width="2"/><circle cx="9" cy="17" r="1.8" fill="#1c1c1c"/><circle cx="17" cy="17" r="1.8" fill="#1c1c1c"/></svg>
      $0.00
    </span>
  </nav>
</header>

<section class="hero">
  <div class="photo hero-photo" role="img" aria-label="Athletic woman in training gear posing against a dark smoky backdrop"></div>
  <div class="hero-copy">
    <h1>Stop dieting and start losing more weight faster!</h1>
    <p>Brivan Fitco is a 100% custom online personal coaching program for those looking to burn fat while building a lean athletic body.</p>
    <span class="btn btn-yellow">Book an appointment</span>
    <div class="dots"><i class="on"></i><i></i><i></i><i></i></div>
  </div>
</section>

<section class="welcome">
  <div class="photo welcome-photo" role="img" aria-label="Personal trainer with a clipboard beside a smiling client holding a water bottle"></div>
  <div class="welcome-copy">
    <div class="kicker">Welcome to</div>
    <h2>Brivan Fitco</h2>
    <p>Our coaches build every plan around your body, your schedule and your goals. From meal plans to training blocks, each step is tailored so you lose fat, gain strength and keep the results for life. No fad diets, no guesswork, just a clear path and a team that checks in with you every week.</p>
    <span class="btn btn-outline">Read more</span>
  </div>
</section>

<section class="help">
  <svg class="abs" style="left:0;top:0" width="1200" height="560" viewBox="0 0 1200 560" aria-hidden="true">
    <polygon points="0,40 1200,0 1200,520 0,560" fill="#1f1f1f"/>
    <polygon points="960,0 1200,0 1200,190 1120,90" fill="var(--yellow)"/>
  </svg>
  <h2>We help you lose<br><span class="hl">weight</span> and keep it <span class="hl">off!*</span></h2>
  <div class="features">
    <div class="feature"><div class="ring"><svg width="28" height="28" viewBox="0 0 28 28"><rect x="6" y="4" width="16" height="20" fill="none" stroke="#fff" stroke-width="2"/><path d="M10 10h8M10 15h8M10 20h5" stroke="#fff" stroke-width="2"/></svg></div>Custom meal plans</div>
    <div class="feature"><div class="ring"><svg width="30" height="20" viewBox="0 0 30 20"><path d="M2 10h26" stroke="#fff" stroke-width="2"/><rect x="4" y="4" width="4" height="12" fill="#fff"/><rect x="22" y="4" width="4" height="12" fill="#fff"/></svg></div>Custom training plans</div>
    <div class="feature"><div class="ring"><svg width="28" height="28" viewBox="0 0 28 28"><circle cx="14" cy="10" r="5" fill="none" stroke="#fff" stroke-width="2"/><path d="M5 25c1-6 5-8 9-8s8 2 9 8" fill="none" stroke="#fff" stroke-width="2"/></svg></div>One on one coaching</div>
  </div>
  <div class="photo help-video" role="img" aria-label="Group class doing plank exercises on mats in a bright gym">
    <div class="play"><svg width="22" height="24" viewBox="0 0 22 24"><polygon points="4,2 20,12 4,22" fill="#1c1c1c"/></svg></div>
  </div>
</section>

<section class="discover">
  <svg class="abs" style="left:0;top:0" width="1200" height="560" viewBox="0 0 1200 560" aria-hidden="true">
    <polygon points="0,0 300,0 120,110 0,200" fill="var(--yellow)"/>
    <polygon points="60,120 1200,80 1200,470 0,500 0,140" fill="var(--dark)"/>
    <polygon points="60,90 330,90 200,160 40,170" fill="#111"/>
    <polygon points="1200,380 1200,560 980,560" fill="var(--yellow)"/>
  </svg>
  <div class="photo discover-video" role="img" aria-label="Group of people stretching outdoors on grass in warm sunlight">
    <div class="play"><svg width="22" height="24" viewBox="0 0 22 24"><polygon points="4,2 20,12 4,22" fill="#1c1c1c"/></svg></div>
  </div>
  <div class="discover-copy">
    <h2>Discover how you can <span class="hl">burn fat and build a lean body at the same time!</span></h2>
    <p>Unlike the average carb-loaded diets that tell you to starve yourself, our method teaches your body to burn stored fat for fuel, keeping energy steady while building lean muscle.</p>
    <span class="btn btn-outline light">Read more</span>
  </div>
</section>

<section class="success">
  <h2>Your success is our success</h2>
  <div class="sub">Don't be just another sale, join a community of like-minded people that want to see you succeed!</div>
  <div class="photo success-photo" role="img" aria-label="Fit woman in sports bra measuring her waist with a tape measure"></div>

  <div class="perk left" style="left:100px;top:360px">
    <div class="perk-head"><h3>Private Online<br>Community</h3>
      <svg width="40" height="40" viewBox="0 0 40 40"><circle cx="14" cy="14" r="5" fill="none" stroke="#333" stroke-width="2"/><circle cx="27" cy="14" r="5" fill="none" stroke="#333" stroke-width="2"/><path d="M5 34c1-7 5-10 9-10s8 3 9 10M20 34c1-7 4-10 7-10s7 3 8 10" fill="none" stroke="#333" stroke-width="2"/></svg></div>
    <p>Join our members-only group where clients share wins, recipes and training tips. Our coaches are active in the group every day to answer questions and keep you on track.</p>
  </div>
  <div class="perk left" style="left:100px;top:600px">
    <div class="perk-head"><h3>Weekly<br>Accountability Calls</h3>
      <svg width="40" height="40" viewBox="0 0 40 40"><path d="M8 30c4-8 8-12 12-12s8 4 12 12" fill="none" stroke="#333" stroke-width="2"/><circle cx="20" cy="11" r="5" fill="none" stroke="#333" stroke-width="2"/></svg></div>
    <p>Each week your coach calls to review progress, adjust your plan and answer any questions so you never feel stuck.</p>
  </div>
  <div class="perk" style="left:800px;top:360px">
    <div class="perk-head">
      <svg width="40" height="40" viewBox="0 0 40 40"><rect x="6" y="8" width="28" height="20" rx="2" fill="none" stroke="#333" stroke-width="2"/><path d="M12 28v6l6-6" fill="none" stroke="#333" stroke-width="2"/></svg>
      <h3>Unlimited<br>Text &amp; Email Support</h3></div>
    <p>Message your coach any time by text or email. You get real answers from a real person, usually the same day, whenever you need guidance.</p>
  </div>
  <div class="perk" style="left:800px;top:600px">
    <div class="perk-head">
      <svg width="40" height="40" viewBox="0 0 40 40"><rect x="5" y="8" width="30" height="22" fill="none" stroke="#333" stroke-width="2"/><path d="M14 34h12M20 30v4" stroke="#333" stroke-width="2"/></svg>
      <h3>Member<br>Portal Access</h3></div>
    <p>Log in to track workouts, view your meal plans, update your stats and find answers in one simple place.</p>
  </div>
</section>

<section class="testimonial">
  <h2><span class="hl">Client</span> <span style="color:#fff">Testimonial</span></h2>
  <div class="clients">
    <div class="client"><div class="avatar" role="img" aria-label="Client portrait"></div><div><b>By John Doe</b><span>Personal Training</span></div></div>
    <div class="client"><div class="avatar" role="img" aria-label="Client portrait"></div><div><b>By John Doe</b><span>Personal Training</span></div></div>
    <div class="client"><div class="avatar" role="img" aria-label="Client portrait"></div><div><b>By John Doe</b><span>Personal Training</span></div></div>
  </div>
  <p class="quote">“I tried every diet out there before joining. Within three months I had dropped two sizes, gained real strength and finally understood how to eat. The weekly calls kept me honest and the plan never felt like a chore.”</p>
  <div class="t-dots"><i class="on"></i><i></i><i></i></div>
</section>

<section class="guarantee">
  <div class="photo guarantee-photo" role="img" aria-label="Smiling woman measuring her waist in front of a brick wall"></div>
  <div class="card">
    <h2>30 Day Money Back Guarantee</h2>
    <p>If you do not experience the results you should by the efforts you put in. We will refund 100% of the cost of the program. So what do you have to lose... besides fat?</p>
    <span class="btn btn-yellow">Get my customized plan</span>
  </div>
</section>

<footer class="site-footer">
  <div class="f-col" style="left:100px">
    <h4>Quick Link</h4>
    <ul>
      <li><span class="bullet"></span>Home</li>
      <li><span class="bullet"></span>About Us</li>
      <li><span class="bullet"></span>Programs</li>
      <li><span class="bullet"></span>Supplements</li>
      <li><span class="bullet"></span>FAQ</li>
      <li><span class="bullet"></span>Contact Us</li>
    </ul>
  </div>
  <div class="f-col" style="left:300px">
    <h4>Contact Us</h4>
    <ul>
      <li><svg width="12" height="16" viewBox="0 0 12 16"><path d="M6 1a5 5 0 0 1 5 5c0 4-5 9-5 9S1 10 1 6a5 5 0 0 1 5-5z" fill="var(--yellow)"/></svg><span>Brivan Fitco<br>2480 Harlow Avenue, Suite 310<br>Cedar Falls, United States</span></li>
      <li><svg width="14" height="14" viewBox="0 0 14 14"><path d="M3 1l3 3-2 2c1 2 2 3 4 4l2-2 3 3-2 2C6 13 1 8 1 3z" fill="var(--yellow)"/></svg>(319) 402-7781</li>
      <li><svg width="14" height="12" viewBox="0 0 14 12"><rect x="1" y="1" width="12" height="10" fill="none" stroke="var(--yellow)" stroke-width="1.5"/><path d="M1 1l6 5 6-5" fill="none" stroke="var(--yellow)" stroke-width="1.5"/></svg>hello@brivanfitco.com</li>
    </ul>
  </div>
  <div class="f-col" style="left:620px">
    <h4>Gym Inquiries</h4>
    <p>Have a question about training, nutrition or our programs? Send us a message and a coach will get back to you within one business day.</p>
    <div class="form">
      <div class="field">Name</div><div class="field">Email Address</div>
      <div class="field">Contact Number</div><div class="btn btn-yellow" style="text-align:center;padding:11px 0">Submit Now!</div>
    </div>
  </div>
  <div class="socials"><i></i><i></i><i></i><i></i></div>
  <div class="copy">© 2024 Brivan Fitco. All Rights Reserved.</div>
</footer>

</body>
</html>
```